Ned Halvorsen Executive Coach Business Card Design

I need a new card design for my Executive Coaching practice. I am a Clinical Psychotherapist and Executive Coach. I help my clients get the most out of life by developing their personal and professional skills and abilities.

I work with senior executives. My design needs to be high end. I am thinking gloss on the front. I am also thinking contemporary. I am going to use a black, grey and red colour scheme on the the website. I am thinking grey with black and red accents. I would also like a water mark included on the card.

Target Market(s)

Senior Executives In major Companies

Industry/Entity Type

Business

Contact Information for Business Card

On the front

Ned Halvorsen
Clinical Psychotherapist and Executive Coach
For Personal and Professional Success

On the Back

Tarwin office
87 Tarwin Vale Road Tarwin

North Sydney Office
Suite 309 / 41 Lathom Street North Sydney

Pellington Street Office
Suite 512 / 218 Pellington Street Sydney CBD

Phone 02 95817364
Email ned@nedhalvorsen.com.au

Requirements
Must have
• Friendly but professional
Water Mark
Gloss Front

```html
<!DOCTYPE html>
<html lang="en">
<head>
<meta charset="utf-8">
<title>Ned Halvorsen – Business Card</title>
<link rel="stylesheet" href="https://fonts.googleapis.com/css2?family=Bree+Serif&display=swap">
<style>
  :root {
    --page: #e9e6e2;
    --card-black: #050505;
    --card-sheen: #4a4a4a;
    --accent-red: #e0141b;
    --text-white: #f4f4f4;
    --text-grey: #cfcfcf;
    --rule-grey: #6a6a6a;
    --watermark: #262626;
  }
  * { margin: 0; padding: 0; box-sizing: border-box; }
  html, body {
    width: 1200px; height: 461px; overflow: hidden;
    background: var(--page);
    font-family: "Bree Serif", Georgia, serif;
  }
  .canvas {
    position: relative; width: 1200px; height: 461px;
    display: flex; justify-content: center; align-items: center; gap: 40px;
  }
  .card {
    position: relative; width: 540px; height: 310px; overflow: hidden;
    background:
      linear-gradient(100deg, var(--card-black) 0%, #1a1a1a 28%, var(--card-sheen) 46%, #1c1c1c 60%, var(--card-black) 100%);
    box-shadow: 0 10px 24px rgba(0,0,0,.35);
  }
  .card::after {
    content: ""; position: absolute; inset: 0;
    background: linear-gradient(180deg, rgba(255,255,255,.08) 0%, rgba(255,255,255,0) 45%);
    pointer-events: none;
  }
  /* Front */
  .card-front { text-align: center; }
  .front-name {
    position: absolute; top: 72px; left: 0; right: 0;
    color: var(--accent-red); font-size: 42px; font-weight: 400; letter-spacing: .5px;
  }
  .front-title {
    position: absolute; top: 126px; left: 0; right: 0;
    color: var(--text-white); font-size: 19px;
  }
  .front-tagline {
    position: absolute; top: 238px; left: 0; right: 0;
    color: var(--text-white); font-size: 19px;
  }
  /* Back */
  .back-name {
    position: absolute; top: 32px; left: 28px;
    color: var(--accent-red); font-size: 30px;
  }
  .back-rule {
    position: absolute; top: 76px; left: 28px; width: 230px; height: 1px;
    background: var(--rule-grey);
  }
  .watermark {
    position: absolute; top: 150px; right: -118px; transform: rotate(90deg);
    width: 300px; text-align: center;
    color: var(--watermark); font-size: 32px; white-space: nowrap;
  }
  .contact { position: absolute; top: 170px; left: 30px; list-style: none; }
  .contact li { color: var(--text-white); font-size: 15px; line-height: 24px; }
  .contact .label { color: var(--accent-red); margin-right: 4px; }
  .offices { position: absolute; top: 232px; left: 30px; list-style: none; }
  .offices li { color: var(--text-grey); font-size: 12.5px; line-height: 21px; }
</style>
</head>
<body>
<main class="canvas">
  <section class="card card-front" aria-label="Card front">
    <h1 class="front-name">Ned Halvorsen</h1>
    <p class="front-title">Clinical Psychotherapist &amp; Executive Coach</p>
    <p class="front-tagline">For Personal &amp; Professional Success</p>
  </section>

  <section class="card card-back" aria-label="Card back">
    <h2 class="back-name">Ned Halvorsen</h2>
    <div class="back-rule"></div>
    <div class="watermark" aria-hidden="true">Ned Halvorsen</div>
    <ul class="contact">
      <li><span class="label">P:</span>02 95817364</li>
      <li><span class="label">E:</span>ned@nedhalvorsen.com.au</li>
    </ul>
    <ul class="offices">
      <li>87 Tarwin Vale Road Tarwin North Sydney</li>
      <li>Suite 512 / 218 Pellington Street Sydney CBD</li>
      <li>Suite 309 / 41 Lathom Street North Sydney Pellington Street</li>
    </ul>
  </section>
</main>
</body>
</html>
```